Require stationery design: letter head and update existing business card

clean, simple, minamilistic, los of negative space, black or white. casual, but passionate, informative and knowledgable , no fuss, don to earth.

logo newly created and supplied As AI files in breif. . TO CONFIRM THE FINAL LOGO IS THE VERSION WITH THE GRAPHIC / PICTURE INCLUDED. we now need to update our business card design, take old logo out and replace with new logo, raw business files supplied in brief.
For business card I need proofs with white, black and ligjt timber / rustic cookie.

Target Market(s)

women, house wives, business men, hospitality, higher socio economic, commercial residential, niche market.

Industry/Entity Type

Business

Number of Pages Required

3 page

Font styles to use
Sans Serif

Colors
ffffff
3277b5
0355a3
faa54b
f68e4e

Requirements
Must have
• proofs for business card design to be provided on white, black, timber / cardboard background. logo and business to be supplied in all usable formats and files.
• Letter head to be A4 against white background. Supplier in WORDDOC or send header and footer images as JPEG so I can insert into word template
• suitable quote, invoice, receipt template for emailed pdf's
Nice to have
• stylised touch. finesse. sophistication. we are competed in this kind of market.
• use the colour featured in the screen shot file of a random logo
Should not have
• clutter. be crowded. more than 2 fonts.

```html
<!DOCTYPE html>
<html lang="en">
<head>
<meta charset="UTF-8">
<title>Timber &amp; Grain Co. — Business Card</title>
<link href="https://fonts.googleapis.com/css2?family=Open+Sans:wght@400;600&display=swap" rel="stylesheet">
<style>
  :root {
    --stage: #2b2b2b;
    --card-black: #1b1b1b;
    --card-white: #ffffff;
    --ink-light: #f2f2f2;
    --ink-dark: #222222;
    --ink-muted: #444444;
  }
  * { box-sizing: border-box; margin: 0; padding: 0; }
  html, body {
    width: 1200px; height: 1200px; overflow: hidden;
    background: var(--stage);
    font-family: "Open Sans", sans-serif;
  }
  .card {
    position: absolute;
    width: 640px; height: 366px;
    box-shadow: 0 14px 30px rgba(0,0,0,0.45);
  }
  .card--front {
    left: 140px; top: 230px;
    background: var(--card-black);
    display: flex; align-items: center; justify-content: center;
  }
  .card--back {
    left: 420px; top: 600px;
    background: var(--card-white);
    display: flex; flex-direction: column; align-items: center; justify-content: center;
    color: var(--ink-dark);
  }
  .brand {
    display: flex; align-items: center; gap: 16px;
    color: var(--ink-light);
  }
  .brand__dot {
    width: 22px; height: 22px; border-radius: 50%;
    background: var(--ink-light);
  }
  .brand__name {
    font-weight: 400;
    font-size: 40px;
    letter-spacing: 3px;
    text-transform: uppercase;
    white-space: nowrap;
  }
  .tagline {
    font-size: 15px; font-weight: 600;
    letter-spacing: 1.2px; text-transform: uppercase;
    margin-bottom: 30px;
    white-space: nowrap;
  }
  .contact { list-style: none; font-size: 17px; color: var(--ink-muted); line-height: 1.55; }
  .contact li { display: flex; align-items: center; gap: 8px; white-space: nowrap; }
  .contact svg { width: 14px; height: 14px; fill: var(--ink-dark); flex: none; }
  .contact li:first-child { justify-content: center; }
</style>
</head>
<body>
  <section class="card card--front">
    <div class="brand">
      <span class="brand__dot"></span>
      <span class="brand__name">Timber &amp; Grain Co.</span>
    </div>
  </section>

  <section class="card card--back">
    <p class="tagline">True Grain Finders &amp; Hardwood Table Makers</p>
    <ul class="contact">
      <li>
        <svg viewBox="0 0 24 24"><path d="M6.6 10.8a15.1 15.1 0 0 0 6.6 6.6l2.2-2.2c.3-.3.7-.4 1-.2 1.1.4 2.3.6 3.6.6.6 0 1 .4 1 1V20c0 .6-.4 1-1 1C10.6 21 3 13.4 3 4c0-.6.4-1 1-1h3.5c.6 0 1 .4 1 1 0 1.3.2 2.5.6 3.6.1.3 0 .7-.2 1z"/></svg>
        021 555 0142
      </li>
      <li>
        <svg viewBox="0 0 24 24"><path d="M2 5h20v14H2z M2 5l10 8 10-8" fill="none" stroke="#222" stroke-width="2"/><path d="M2 5h20L12 13z"/></svg>
        info@timberandgrain.com.nz
      </li>
      <li>
        <svg viewBox="0 0 24 24"><circle cx="12" cy="12" r="9" fill="none" stroke="#222" stroke-width="2"/><path d="M3 12h18M12 3c3 3 3 15 0 18M12 3c-3 3-3 15 0 18" fill="none" stroke="#222" stroke-width="1.6"/></svg>
        www.timberandgrain.com.nz
      </li>
    </ul>
  </section>
</body>
</html>
```